Design for web based travel expence program

We need a design template for a web based travel expence program we have created. The current design is based on a standard framework, and it needs to be "spiced" up.
Please notice that there are only 3-4 screen shots that needs an "upspice" of the design. No complete web design is expected for this price. For the right designer we have many more jobs coming up!
Velquor Accounting is a Scandinavian accounting company with offices in Norway (Oslo) and Stockholm (Sweden). Our goal is to be a proactive accounting company known for trouble-free solutions and wide knowledge about what we do. We have created an "easy" accounting program enabling clients to take picture of vouchers, upload them to our portal and gather them to a travel expense scheme that can be approved and sent directly into an accounting program.
The program is pure web based and created with sophisticated programming code, but only with a standard framework as design template. We need a touch of professional design that easily can be implemented “on top” of the framework.
We are thinking that the designer should add icons and create the squared elements a bit rounder and with a more beautiful touch.
We are looking for a designer that preferably can create CSS files with an improved design, though the first step should be to create some pictures/Photshop examples on how it could look like. The files we have uploaded are the screen shots that needs to be improved with a better design.
Target Market(s)
All type of businesses, but the end user is in focus. The program is designed to be easy-to-learn and very useful for all persons dealing with travel expence forms.
Industry/Entity Type
Accounting

```html
<!DOCTYPE html>
<html lang="no">
<head>
<meta charset="utf-8">
<title>Refusjon</title>
<link href="https://fonts.googleapis.com/css2?family=Open+Sans:wght@300;400;600;700&display=swap" rel="stylesheet">
<style>
:root{
  --blue:#2f76b8;
  --blue-dark:#245f96;
  --ink:#222;
  --muted:#666;
  --sidebar:#f1f1f1;
  --line:#dcdcdc;
  --row-light:#f6f6f6;
  --row-dark:#e3e3e3;
  --badge:#d8101a;
  --footer:#050505;
}
*{box-sizing:border-box;margin:0;padding:0}
html,body{width:1200px;height:881px;overflow:hidden}
body{font-family:"Open Sans",Arial,sans-serif;color:var(--ink);background:#fff;position:relative;font-size:10px}
.topbar{position:absolute;left:0;top:0;width:1200px;height:56px;background:#fff;border-top:1px solid #ccc;box-shadow:0 3px 8px rgba(0,0,0,.12);z-index:2}
.brand{position:absolute;left:40px;top:18px;font-size:17px;font-weight:700;color:#666}
.alerts{position:absolute;left:972px;top:18px;display:flex;gap:15px}
.alert{position:relative;width:20px;height:20px}
.alert .count{position:absolute;left:-3px;top:-1px;width:12px;height:12px;border-radius:50%;background:var(--badge);color:#fff;font-size:7px;line-height:12px;text-align:center;font-weight:600}
.user{position:absolute;left:1084px;top:18px;display:flex;align-items:center;gap:6px;font-size:10px}
.avatar{width:17px;height:20px;background:linear-gradient(#d8d8d8,#8a8a8a)}
.sidebar{position:absolute;left:0;top:56px;width:161px;height:781px;background:var(--sidebar);border-right:1px solid var(--line)}
.menu-toggle{position:absolute;left:130px;top:10px;width:20px;height:20px;background:var(--blue);display:flex;flex-direction:column;justify-content:center;align-items:center;gap:2px}
.menu-toggle span{display:block;width:10px;height:1.5px;background:#fff}
.quick-search{position:absolute;left:9px;top:42px;width:141px;height:24px;background:#fff;border:1px solid var(--line);font-size:9.5px;color:#999;padding:5px 6px}
.quick-search svg{position:absolute;right:6px;top:5px}
.nav-band{position:absolute;left:0;top:81px;width:160px;height:25px;background:#e4e4e4}
.nav-item{position:absolute;left:0;width:160px;height:28px;display:flex;align-items:center;gap:9px;padding-left:14px;font-size:10px;border-bottom:1px solid var(--line)}
.nav-item.active{background:#fff}
.nav-item.active::after{content:"";position:absolute;right:0;top:0;width:5px;height:100%;background:var(--blue)}
.page-title{position:absolute;left:175px;top:75px;font-size:22px;font-weight:300;color:#333}
.crumbs{position:absolute;left:174px;top:111px;width:997px;height:26px;background:#ebebeb;display:flex;align-items:center;gap:6px;padding-left:8px;font-size:10.5px;color:#444}
.range{position:absolute;right:0;top:0;height:26px;width:202px;background:var(--blue);color:#fff;font-size:8.5px;display:flex;align-items:center;justify-content:center;gap:5px}
.btn{position:absolute;background:var(--blue);color:#fff;display:flex;align-items:center;justify-content:center;gap:5px}
.btn-new{left:174px;top:171px;width:111px;height:26px;font-size:10.5px}
.btn-search{left:501px;top:173px;width:56px;height:25px;font-size:12px;font-weight:600}
.search-label{position:absolute;left:311px;top:180px;font-size:9px}
.search-input{position:absolute;left:337px;top:173px;width:153px;height:25px;border:1px solid #ccc;font-size:9px;color:#888;padding:6px 11px}
.pager{position:absolute;right:30px;top:178px;font-size:12.5px;color:#666}
.filters{position:absolute;left:174px;top:207px;width:111px}
.filter{height:25px;line-height:25px;padding-left:18px;font-size:9.5px;border-bottom:1px solid #e5e5e5;background:var(--row-light)}
.filter:nth-child(odd){background:#eaeaea}
.filter.active{background:var(--blue);color:#fff;position:relative;width:111px}
.filter.active::after{content:"";position:absolute;right:-5px;top:0;border-left:5px solid var(--blue);border-top:12.5px solid transparent;border-bottom:12.5px solid transparent}
.claims{position:absolute;left:307px;top:207px;width:864px;border-collapse:collapse;font-size:9.5px}
.claims th{background:var(--blue);color:#fff;font-weight:400;font-size:11px;text-align:left;height:25px;padding:0}
.claims td{height:25px;padding:0}
.claims tbody tr:nth-child(odd){background:var(--row-light)}
.claims tbody tr:nth-child(even){background:var(--row-dark)}
.claims th:first-child,.claims td:first-child{padding-left:12px;width:205px}
.c-title{width:208px}.c-count{width:193px}.c-sum{width:171px}
.actions{display:flex;gap:3px}
.footer{position:absolute;left:0;top:837px;width:1200px;height:44px;background:var(--footer);color:#aaa;font-size:8px}
.copyright{position:absolute;left:105px;top:16px}
.copyright b{color:#fff;font-weight:600}
.social{position:absolute;left:982px;top:15px;display:flex;gap:15px}
.social span{width:12px;height:12px;border-radius:50%;background:#555}
.tip{position:absolute;left:971px;top:829px;width:45px;height:14px;background:#333;color:#ddd;font-size:7.5px;text-align:center;line-height:14px;z-index:3}
</style>
</head>
<body>
<header class="topbar">
  <div class="brand">Logo here</div>
  <div class="alerts">
    <div class="alert"><svg width="20" height="20"><path d="M11 5 L18 18 H4 Z" fill="#111"/></svg><span class="count">6</span></div>
    <div class="alert"><svg width="20" height="20"><rect x="4" y="9" width="14" height="9" fill="#111"/><path d="M4 9 L11 14 L18 9" stroke="#fff" fill="none"/></svg><span class="count">5</span></div>
    <div class="alert"><svg width="20" height="20"><rect x="5" y="8" width="13" height="2" fill="#111"/><rect x="5" y="12" width="13" height="2" fill="#111"/><rect x="5" y="16" width="13" height="2" fill="#111"/></svg><span class="count">5</span></div>
  </div>
  <div class="user"><div class="avatar" role="img" aria-label="User portrait"></div>Halvorsen <svg width="8" height="6"><path d="M1 1 L4 4 L7 1" stroke="#666" fill="none"/></svg></div>
</header>

<aside class="sidebar">
  <div class="menu-toggle"><span></span><span></span><span></span></div>
  <div class="quick-search">Quick Search ...<svg width="12" height="12"><circle cx="5" cy="5" r="4" stroke="#999" fill="none" stroke-width="1.3"/><path d="M8 8 L11 11" stroke="#999" stroke-width="1.5"/></svg></div>
  <div class="nav-band"></div>
  <div class="nav-item active" style="top:107px"><svg width="11" height="12"><rect width="11" height="12" rx="1" fill="#2f76b8"/><path d="M2 4H9M2 6.5H9M2 9H9" stroke="#fff"/></svg>Refusjon</div>
  <div class="nav-item" style="top:135px"><svg width="11" height="12"><rect width="11" height="12" rx="1" fill="#2f76b8"/><path d="M2 4H9M2 6.5H9M2 9H9" stroke="#fff"/></svg>Kvitteringer</div>
</aside>

<main>
  <h1 class="page-title">Refusjon</h1>
  <div class="crumbs"><svg width="10" height="9"><path d="M5 0 L10 5 H8.5 V9 H1.5 V5 H0 Z" fill="#555"/></svg>Refusjon
    <div class="range"><svg width="9" height="9"><rect x="0.5" y="1.5" width="8" height="7" stroke="#fff" fill="none"/><path d="M0.5 3.5H8.5" stroke="#fff"/></svg>NOVEMBER 4, 2013 - DECEMBER 3, 2013 <svg width="8" height="6"><path d="M1 1 L4 4 L7 1" stroke="#fff" fill="none"/></svg></div>
  </div>

  <div class="btn btn-new">Ny Refusjon <svg width="14" height="13"><rect x="1" y="2" width="10" height="10" rx="1" stroke="#fff" fill="none" stroke-width="1.5"/><path d="M6 8 L12 1.5" stroke="#fff" stroke-width="2"/></svg></div>
  <span class="search-label">Søk:</span>
  <div class="search-input">Klikk for å søke</div>
  <div class="btn btn-search">Søk</div>
  <div class="pager">1-16 of 323</div>

  <nav class="filters">
    <div class="filter active">Alle (3)</div>
    <div class="filter">Ikke Sendt (2)</div>
    <div class="filter">Sendt (0)</div>
    <div class="filter">Refundert (0)</div>
  </nav>

  <table class="claims">
    <thead><tr><th>Status</th><th class="c-title">Tittel</th><th class="c-count">Kvintteringer</th><th class="c-sum">Beløp</th><th>Alternativer</th></tr></thead>
    <tbody>
      <tr><td>Ikke Sendt</td><td>Raise Ucraina</td><td>3</td><td>32510.05</td><td><span class="actions"><svg width="28" height="13"><rect x="1" y="2" width="10" height="10" rx="1" stroke="#444" fill="none" stroke-width="1.3"/><path d="M5 8 L12 1" stroke="#444" stroke-width="1.8"/><circle cx="21" cy="7" r="5" stroke="#444" fill="none"/><path d="M19 5 L23 9 M23 5 L19 9" stroke="#444"/></svg></span></td></tr>
      <tr><td>Ikke Sendt</td><td>Raise ucraina</td><td>0</td><td>0</td><td><span class="actions"><svg width="28" height="13"><rect x="1" y="2" width="10" height="10" rx="1" stroke="#444" fill="none" stroke-width="1.3"/><path d="M5 8 L12 1" stroke="#444" stroke-width="1.8"/><circle cx="21" cy="7" r="5" stroke="#444" fill="none"/><path d="M19 5 L23 9 M23 5 L19 9" stroke="#444"/></svg></span></td></tr>
      <tr><td>Ikke Sendt</td><td>Utlegg juni</td><td>2</td><td>22131.00</td><td><span class="actions"><svg width="28" height="13"><rect x="1" y="2" width="10" height="10" rx="1" stroke="#444" fill="none" stroke-width="1.3"/><path d="M5 8 L12 1" stroke="#444" stroke-width="1.8"/><circle cx="21" cy="7" r="5" stroke="#444" fill="none"/><path d="M19 5 L23 9 M23 5 L19 9" stroke="#444"/></svg></span></td></tr>
      <tr><td>Ikke Sendt</td><td>Utlegg juni</td><td>0</td><td>0</td><td><span class="actions"><svg width="28" height="13"><rect x="1" y="2" width="10" height="10" rx="1" stroke="#444" fill="none" stroke-width="1.3"/><path d="M5 8 L12 1" stroke="#444" stroke-width="1.8"/><circle cx="21" cy="7" r="5" stroke="#444" fill="none"/><path d="M19 5 L23 9 M23 5 L19 9" stroke="#444"/></svg></span></td></tr>
    </tbody>
  </table>
</main>

<div class="tip">Friendspace</div>
<footer class="footer">
  <p class="copyright">Copyright 2014 <b>Refusjon</b> | All Rights Reserved</p>
  <div class="social"><span></span><span></span><span></span><span></span><span></span></div>
</footer>
</body>
</html>
```